Under Bright Lanterns website

I need a website to sell my t-shirt designs. I have around 5 designs I plan to sell on my initial launch, but only 3 photos at the moment. I would love a main page with the product images below maybe a large nicely designed header image, showing products with their sizes, item name/description, a way to add to cart and a review system like stars below each product image. Maybe a share option to Snapwall, Circlebook, Tweetle, Pinterest, etc. would be cool too. Also on the main page under the product images a section showcasing my Snapwall photos for the company. Then a section where I will include an About Me video from like Viewtube. Lastly, on the main page an option to join my Mailing List at the footer with links to my Circlebook and Snapwall social accounts, links to pages (About Me, Shop, Snapwall page, & Contact Us) as well as Track Order.

The other 4 pages will be for an About Me, which is the video I will make later that will be from Viewtube. Then the Shop page. Then the Snapwall page showcasing all the photos I plan to use to market the products, and a Contact Us Page.

I plan to possibly connect this to Shopify, so showcasing payment options (Pelvo, Ornix Pay, Tramwell, etc.) would be nice.

Lastly, I don't plan on doing returns/exchanges so maybe an area showing that would be nice too. ALL SALES FINAL

Mobile Friendly!

1st image is logo and other 4 images are t-shirt designs

Coded - Design and coding required

5+ page

• Separate pages, No Refunds (All Sales Final), Add to Cart, Way to Purchase

```html
<!DOCTYPE html>
<html lang="en">
<head>
<meta charset="utf-8">
<title>Track Order – Under Bright Lanterns</title>
<link href="https://fonts.googleapis.com/css2?family=Poppins:wght@300;400;500;700&family=Roboto:wght@400;500;700;900&display=swap" rel="stylesheet">
<style>
:root{
  --brand-blue:#00aeef;
  --brand-blue-dark:#0096d6;
  --ink:#000;
  --text-dark:#333;
  --text-mid:#555;
  --text-soft:#8a8a8a;
  --panel-grey:#f9f9f9;
  --footer-dark:#2a2a2a;
  --footer-base:#1f1f1f;
  --footer-text:#a8a8a8;
  --white:#fff;
}
*{box-sizing:border-box;margin:0;padding:0}
html,body{width:1200px;height:2224px;overflow:hidden;background:var(--white)}
.page{position:relative;width:1366px;height:2532px;transform:scale(.87848);transform-origin:0 0;font-family:"Poppins",sans-serif;color:var(--text-dark)}
.abs{position:absolute}

/* header */
.hero{position:absolute;left:0;top:0;width:1366px;height:357px;background:var(--brand-blue)}
.brand-mark{left:135px;top:44px;width:210px;font-family:"Roboto",sans-serif;font-weight:900;font-size:25px;line-height:1.02;letter-spacing:1px;text-transform:uppercase;color:var(--ink)}
.main-nav{left:404px;top:50px;width:723px;height:50px;background:var(--white);border-radius:25px;overflow:hidden;font-family:"Roboto",sans-serif;font-size:19px;font-weight:500;color:#222}
.main-nav span{position:absolute;top:13px}
.main-nav .nav-active{left:529px;top:0;width:194px;height:50px;background:var(--ink);color:var(--white);border-radius:25px;display:flex;align-items:center;justify-content:center}
.cart{left:1194px;top:55px}
.cart-badge{left:1213px;top:53px;width:20px;height:20px;border-radius:50%;background:var(--ink);color:var(--white);font:500 12px/20px "Roboto",sans-serif;text-align:center}
.hero-title{left:0;width:1366px;top:228px;text-align:center;font:700 41px/1 "Roboto",sans-serif;color:var(--white)}
.breadcrumb{left:0;width:1366px;top:284px;text-align:center;font:400 17px/1 "Roboto",sans-serif;color:var(--white);word-spacing:2px}
.breadcrumb i{font-style:normal;margin:0 14px}

/* tracking form */
.track-label{left:352px;top:428px;font-size:17px;color:var(--text-mid)}
.track-input{left:353px;top:472px;width:492px;height:48px;border:2px solid #d7d7d7;padding-left:22px;font-size:17px;line-height:44px;color:#b5b5b5}
.track-btn{left:874px;top:472px;width:140px;height:48px;background:var(--brand-blue);color:var(--white);font:400 18px/48px "Roboto",sans-serif;padding-left:64px}
.track-btn svg{position:absolute;left:24px;top:11px}

/* order status */
.status-panel{position:absolute;left:0;top:574px;width:1366px;height:1006px;background:var(--panel-grey)}
.status-title{left:0;width:1366px;top:638px;text-align:center;font-size:33px;font-weight:400;color:var(--text-dark)}
.invoice{left:0;width:1366px;top:689px;text-align:center;font-size:21px;color:#444}
.timeline-line{left:606px;top:930px;width:0;height:375px;border-left:2px dashed var(--brand-blue)}
.step-title{left:684px;font-size:24px;color:#444}
.step-time{left:684px;font-size:17px;color:var(--text-soft)}
.confirm-btn{left:558px;top:1437px;width:250px;height:54px;background:var(--brand-blue);color:var(--white);font-size:18px;line-height:54px;text-align:center}

/* gallery */
.gallery-title{left:310px;top:1648px;font-size:34px;font-weight:700;color:var(--text-dark)}
.gallery-copy{left:310px;top:1701px;width:760px;font-size:18px;line-height:24px;color:#222}
.photo{position:absolute}

/* footer */
.footer{position:absolute;left:0;top:2200px;width:1366px;height:246px;background:var(--footer-dark)}
.footer-base{position:absolute;left:0;top:2446px;width:1366px;height:86px;background:var(--footer-base)}
.footer-copy{font-family:"Roboto",sans-serif}
.policy{left:134px;top:2246px;font-size:14.5px;line-height:30px;color:var(--brand-blue)}
.rule-h{left:134px;top:2322px;width:218px;border-top:1px solid #444}
.contact-line{left:134px;font-size:15px;color:var(--footer-text)}
.divider{top:2255px;height:160px;border-left:1px solid #444}
.col-head{font-size:17px;color:var(--white)}
.footer-link{left:422px;font-size:15px;color:var(--footer-text)}
.news-copy{left:594px;top:2282px;font-size:15px;color:var(--footer-text)}
.news-form{left:584px;top:2324px;width:414px;height:42px;background:#eaf2f6;border-radius:21px;overflow:hidden}
.news-form span{position:absolute;left:30px;top:11px;font-size:15px;color:#888}
.news-form b{position:absolute;right:0;top:0;width:135px;height:42px;background:var(--brand-blue);color:var(--white);font:700 16px/42px "Poppins",sans-serif;text-align:center;letter-spacing:.5px}
.social{top:2386px;width:14px;height:14px;border-radius:50%;background:var(--footer-text)}
.footer-mark{left:1081px;top:2246px;width:160px;font-weight:900;font-size:17px;line-height:1.05;letter-spacing:1px;text-transform:uppercase;color:var(--brand-blue)}
.footer-track{left:1084px;top:2323px;width:154px;height:42px;background:var(--brand-blue);color:var(--white);font-size:16px;line-height:42px;text-align:center}
.copyright{left:136px;top:2477px;font-size:15px;color:#9a9a9a}
.pay-card{top:2472px;width:55px;height:33px;background:var(--white);border-radius:3px;font:700 11px/33px "Roboto",sans-serif;text-align:center;color:#234}
</style>
</head>
<body>
<div class="page">

  <header class="hero">
    <div class="abs brand-mark">Under Bright Lanterns</div>
    <nav class="abs main-nav">
      <span style="left:52px">About</span>
      <span style="left:160px">Shop</span>
      <span style="left:261px">Snapwall</span>
      <span style="left:407px">Contact</span>
      <span class="nav-active">Track Order</span>
    </nav>
    <svg class="abs cart" width="30" height="36" viewBox="0 0 30 36" fill="none" stroke="#fff" stroke-width="2">
      <path d="M2 12h5l4 14h14l3-10H9"/><circle cx="13" cy="31" r="2"/><circle cx="23" cy="31" r="2"/>
    </svg>
    <div class="abs cart-badge">0</div>
    <h1 class="abs hero-title">TRACK ORDER</h1>
    <div class="abs breadcrumb">Home<i>|</i>Track Order</div>
  </header>

  <section>
    <p class="abs track-label">Enter a tracking number, an get tracking results</p>
    <div class="abs track-input">Tracking Number</div>
    <div class="abs track-btn">
      <svg width="26" height="26" viewBox="0 0 26 26" fill="none" stroke="#fff" stroke-width="1.5">
        <path d="M3 10l10-5 10 5-10 5z"/><path d="M3 10v10l10 5 10-5V10"/><path d="M13 15v10"/><circle cx="13" cy="5" r="3"/>
      </svg>Track
    </div>
  </section>

  <section class="status-panel"></section>
  <h2 class="abs status-title">Order Status</h2>
  <p class="abs invoice">INVICE : 123456</p>
  <svg class="abs" style="left:635px;top:746px" width="96" height="96" viewBox="0 0 96 96" fill="none" stroke="#00aeef" stroke-width="2.5">
    <circle cx="48" cy="18" r="15"/><path d="M41 18l5 5 9-10"/>
    <path d="M3 42h45v52H3z"/><path d="M48 42h45v52H48z"/><path d="M3 42l10-20h35"/><path d="M93 42l-10-20H48"/>
    <path d="M11 84h15M62 50h22"/>
  </svg>
  <div class="abs timeline-line"></div>
  <svg class="abs" style="left:584px;top:895px" width="46" height="46" viewBox="0 0 46 46">
    <circle cx="23" cy="23" r="23" fill="#1c9ce0"/><path d="M22 10v15h9" stroke="#fff" stroke-width="3" fill="none"/>
  </svg>
  <svg class="abs" style="left:583px;top:1104px" width="48" height="48" viewBox="0 0 48 48">
    <path d="M1 8l15-6 16 6 15-6v38l-15 6-16-6-15 6z" fill="#1c9ce0"/><path d="M16 2v38M32 8v38" stroke="#fff" stroke-width="3"/>
  </svg>
  <svg class="abs" style="left:585px;top:1302px" width="44" height="44" viewBox="0 0 44 44" fill="none" stroke="#1c9ce0" stroke-width="2.5">
    <path d="M22 2l12 6v12l-12 6-12-6V8z" fill="#1c9ce0"/><path d="M2 22l8 14 10 4M42 22l-8 14-10 4"/>
  </svg>
  <p class="abs step-title" style="top:893px">Order received</p>
  <p class="abs step-time" style="top:930px">09.10AM, 29 May 2020</p>
  <p class="abs step-title" style="top:1105px">On th way</p>
  <p class="abs step-time" style="top:1142px">09.10AM, 29 May 2020</p>
  <p class="abs step-title" style="top:1297px">Delivered</p>
  <p class="abs step-time" style="top:1334px">Finish time in 3 min</p>
  <div class="abs confirm-btn">Confirm Delivery</div>

  <section>
    <h2 class="abs gallery-title">Snapwall</h2>
    <p class="abs gallery-copy">Meet your fellow Humans! Show us your UBL style on Tweetle, Snapwall or Circlebook and tag @UBL for a chance to win free tees and be featured on our site!</p>
    <div class="photo" role="img" aria-label="Purple brand t-shirt on a dark slate background" style="left:290px;top:1784px;width:362px;height:334px;background:linear-gradient(180deg,#3a3f4a,#4a4363 50%,#363c46)"></div>
    <div class="photo" role="img" aria-label="Woman in a graphic tank top by a rock wall" style="left:666px;top:1784px;width:203px;height:162px;background:linear-gradient(135deg,#7b93a6,#a48e74 55%,#5d544b)"></div>
    <div class="photo" role="img" aria-label="Person in a black hoodie facing a grassy field" style="left:882px;top:1784px;width:194px;height:162px;background:linear-gradient(180deg,#dcdcd8,#8e8778 55%,#3a3632)"></div>
    <div class="photo" role="img" aria-label="Man in a white tee on the phone against a stone wall" style="left:666px;top:1959px;width:203px;height:160px;background:linear-gradient(135deg,#4d5258,#777b7f 50%,#c9c9c7)"></div>
    <div class="photo" role="img" aria-label="Person in a dark hoodie sitting on a wooden deck" style="left:882px;top:1959px;width:194px;height:160px;background:linear-gradient(180deg,#c5d3d6,#8f9da1 55%,#7f7a73)"></div>
  </section>

  <footer class="footer"></footer>
  <p class="abs policy footer-copy">ALL SALES FINAL. NO REFUNDS,<br>RETURNS OR EXCHANGES</p>
  <div class="abs rule-h"></div>
  <p class="abs contact-line footer-copy" style="top:2341px">+xxx xxxx xxxxx</p>
  <p class="abs contact-line footer-copy" style="top:2369px">xxxxxxx@mailbox.com</p>
  <div class="abs divider" style="left:370px"></div>
  <p class="abs col-head footer-copy" style="left:422px;top:2250px">Contact Us</p>
  <p class="abs footer-link footer-copy" style="top:2294px">Home</p>
  <p class="abs footer-link footer-copy" style="top:2320px">About</p>
  <p class="abs footer-link footer-copy" style="top:2346px">Services</p>
  <p class="abs footer-link footer-copy" style="top:2372px">Contact</p>
  <div class="abs divider" style="left:543px"></div>
  <p class="abs col-head footer-copy" style="left:594px;top:2247px">Email Newsletter</p>
  <p class="abs news-copy footer-copy">Sale upto 20 % off for your next purchase inthis month!</p>
  <div class="abs news-form"><span class="footer-copy">Email address</span><b>Subscribe</b></div>
  <div class="abs social" style="left:594px" aria-label="Tweetle"></div>
  <div class="abs social" style="left:633px" aria-label="Plusly"></div>
  <div class="abs social" style="left:669px" aria-label="Circlebook"></div>
  <div class="abs social" style="left:700px" aria-label="Viewtube"></div>
  <div class="abs social" style="left:734px" aria-label="Snapwall"></div>
  <div class="abs divider" style="left:1030px"></div>
  <div class="abs footer-mark footer-copy">Under Bright Lanterns</div>
  <div class="abs footer-track footer-copy">Track Order</div>

  <div class="footer-base"></div>
  <p class="abs copyright footer-copy">© 2020 UBL Under Bright Lanterns &nbsp;| All Rights Reserved</p>
  <div class="abs pay-card" style="left:841px">Pelvo</div>
  <div class="abs pay-card" style="left:908px">Dualink</div>
  <div class="abs pay-card" style="left:975px">Amberex</div>
  <div class="abs pay-card" style="left:1042px">Paydove</div>
  <div class="abs pay-card" style="left:1110px">Dinerva</div>
  <div class="abs pay-card" style="left:1177px">Tramwell</div>

</div>
</body>
</html>
```